Cedar Hollow Counseling, LLC
Business Card Design
Simple
Daniel Korbe
Licensed Clinical Professional Counselor (LCPC)
1587 E. Pine Avenue Suite 1 Bozeman, MT 59715
daniel@cedarhollowtherapy-example.com
www.cedarhollowtherapy-example.com

```html
<!DOCTYPE html>
<html lang="en">
<head>
<meta charset="utf-8">
<title>Cedar Hollow Counseling, LLC — Business Card</title>
<link href="https://fonts.googleapis.com/css2?family=Montserrat:wght@400;500;600;700&display=swap" rel="stylesheet">
<style>
  :root {
    --backdrop: #d9d9d9;
    --card-white: #ffffff;
    --card-black: #15171a;
    --navy: #1d2f55;
    --text-grey: #5a6170;
    --rule: #b7bcc6;
    --edge-blue: #2a4a8c;
    --emboss: #2b2e33;
  }
  * { margin: 0; padding: 0; box-sizing: border-box; }
  html, body { width: 1200px; height: 802px; overflow: hidden; }
  body {
    background: var(--backdrop);
    font-family: "Montserrat", Arial, sans-serif;
    display: flex;
    align-items: center;
    justify-content: center;
    gap: 60px;
  }
  .card {
    width: 510px;
    height: 292px;
    position: relative;
    box-shadow: 0 10px 28px rgba(0,0,0,0.18);
    border-bottom: 3px solid var(--edge-blue);
  }
  .card-front { background: var(--card-white); padding: 40px 38px; }
  .card-back {
    background: var(--card-black);
    display: flex; align-items: center; justify-content: center;
  }
  .brand-name {
    font-weight: 600;
    color: var(--navy);
    text-transform: uppercase;
    letter-spacing: 0.06em;
    line-height: 1.15;
  }
  .card-front .brand-name { font-size: 17px; width: 220px; }
  .card-back .brand-name {
    color: var(--emboss);
    font-size: 30px;
    text-align: center;
    width: 380px;
  }
  .contact-block {
    position: absolute;
    left: 38px; right: 38px; bottom: 34px;
    display: flex;
    gap: 22px;
  }
  .person { flex: 1; }
  .person-name {
    font-weight: 700; color: var(--navy); font-size: 15px;
    text-transform: uppercase; letter-spacing: 0.04em;
  }
  .person-title { font-size: 9.5px; color: var(--text-grey); margin: 4px 0 14px; }
  .contact-list { list-style: none; font-size: 9.5px; color: var(--text-grey); }
  .contact-list li { display: flex; align-items: center; gap: 7px; margin-top: 4px; }
  .contact-list svg { width: 9px; height: 9px; fill: var(--navy); flex-shrink: 0; }
  .address {
    border-left: 1px solid var(--rule);
    padding-left: 14px;
    font-size: 9.5px; color: var(--text-grey); line-height: 1.6;
    align-self: flex-start;
    width: 150px;
  }
</style>
</head>
<body>
  <article class="card card-front">
    <div class="brand-name">Cedar Hollow Counseling, LLC</div>
    <div class="contact-block">
      <div class="person">
        <div class="person-name">Daniel Korbe</div>
        <div class="person-title">Licensed Clinical Professional Counselor (LCPC)</div>
        <ul class="contact-list">
          <li><svg viewBox="0 0 10 10"><path d="M2 0.5l2 2-1 1.2a6 6 0 0 0 3.3 3.3l1.2-1 2 2-1.3 1.5C4.5 9.5 0.5 5.5 0.5 1.8z"/></svg>(406) 555-0142</li>
          <li><svg viewBox="0 0 10 10"><path d="M0.5 2h9v6h-9z M0.5 2l4.5 3.5 4.5-3.5" fill="none" stroke="#1d2f55" stroke-width="1"/></svg>daniel@cedarhollowtherapy-example.com</li>
          <li><svg viewBox="0 0 10 10"><circle cx="5" cy="5" r="4.5"/></svg>www.cedarhollowtherapy-example.com</li>
        </ul>
      </div>
      <div class="address">1587 E. Pine Avenue Suite 1<br>Bozeman, MT 59715</div>
    </div>
  </article>
  <article class="card card-back">
    <div class="brand-name">Cedar Hollow Counseling, LLC</div>
  </article>
</body>
</html>
```